Need a business card for my new home staging and redesign business. Business name: Larkspurrow Interiors. Subtitle: Home styling and staging wizardry

Target Market(s)

Realtors, home sellers

Industry/Entity Type

Real Estate

Contact Information for Business Card

I don't have a website address yet, or a business Facebook account, but would like to include those. Do not have a logo or any graphics

Font styles to use
Sans Serif

Colors

Designer to choose colors to be used in the design.

Requirements
Must have
• Placeholders for contact details, e.g. Phone, email, web address, etc.
Nice to have
• Sophisticated but somewhat whimsical feel. Perhaps a stylized star (or magic wand?) over the "I" in interiors to convey inspiration.
Should not have
• Nothing too cutesy, including cartoon wizards.

```html
<!DOCTYPE html>
<html lang="en">
<head>
<meta charset="utf-8">
<title>Larkspurrow Interiors – Business Card</title>
<link href="https://fonts.googleapis.com/css2?family=Josefin+Sans:wght@600;700&family=Open+Sans:wght@400;600&display=swap" rel="stylesheet">
<style>
  :root {
    --backdrop: #e4e6ea;
    --royal-blue: #1b35b0;
    --bright-blue: #0f6fd4;
    --wedge-blue: #1c39b8;
    --paper: #ffffff;
    --wordmark-blue: #1565d0;
  }
  * { margin: 0; padding: 0; box-sizing: border-box; }
  html, body { width: 1200px; height: 977px; overflow: hidden; }
  body {
    background: var(--backdrop);
    position: relative;
    font-family: "Open Sans", Arial, sans-serif;
  }
  .card {
    position: absolute;
    left: 210px;
    width: 780px;
    height: 446px;
    overflow: hidden;
    box-shadow: 0 6px 22px rgba(0,0,0,0.18);
  }
  .card--front { top: 28px; background: var(--royal-blue); display: flex; align-items: center; justify-content: center; }
  .card--back { top: 503px; background: var(--paper); }

  .wordmark {
    font-family: "Josefin Sans", Arial, sans-serif;
    font-weight: 700;
    text-transform: uppercase;
    text-align: center;
    line-height: 1.05;
    letter-spacing: 0.06em;
  }
  .card--front .wordmark { color: var(--paper); font-size: 54px; }

  .contact-panel {
    position: absolute; left: 0; top: 0;
    width: 366px; height: 100%;
    background: var(--bright-blue);
    color: var(--paper);
    padding: 150px 0 0 82px;
  }
  .person-name { font-size: 25px; font-weight: 600; line-height: 1.1; }
  .person-role { font-size: 14px; font-weight: 600; margin-top: 4px; }
  .contact-list { list-style: none; margin-top: 26px; }
  .contact-list li { display: flex; align-items: center; gap: 16px; font-size: 14px; height: 25px; }
  .contact-list svg { width: 14px; height: 14px; flex: none; fill: var(--paper); }

  .divider-wedge { position: absolute; left: 366px; top: 0; width: 50px; height: 100%; }
  .card--back .wordmark {
    position: absolute; left: 416px; right: 0; top: 0; bottom: 0;
    display: flex; align-items: center; justify-content: center;
    color: var(--wordmark-blue); font-size: 38px;
  }
</style>
</head>
<body>
  <section class="card card--front">
    <div class="wordmark">Larkspurrow<br>Interiors</div>
  </section>

  <section class="card card--back">
    <div class="contact-panel">
      <p class="person-name">Maren Holt</p>
      <p class="person-role">General Manager</p>
      <ul class="contact-list">
        <li><svg viewBox="0 0 24 24"><path d="M6.6 10.8a15.1 15.1 0 0 0 6.6 6.6l2.2-2.2c.3-.3.7-.4 1-.2 1.1.4 2.3.6 3.6.6.6 0 1 .4 1 1V20c0 .6-.4 1-1 1A17 17 0 0 1 3 4c0-.6.4-1 1-1h3.5c.6 0 1 .4 1 1 0 1.3.2 2.5.6 3.6.1.3 0 .7-.2 1z"/></svg>(555) 018 2746</li>
        <li><svg viewBox="0 0 24 24"><path d="M12 5C7 5 2.5 7 1 10l3 3 4-1.5V9c2.6-.8 5.4-.8 8 0v2.5l4 1.5 3-3C21.5 7 17 5 12 5zM6 14l-2 6h16l-2-6H6zm6 1.5a2 2 0 1 1 0 4 2 2 0 0 1 0-4z"/></svg>(555) 018 2747</li>
        <li><svg viewBox="0 0 24 24"><path d="M2 5h20v14H2zM4 7v.4l8 5.2 8-5.2V7z"/></svg>hello@larkspurrow.com</li>
        <li><svg viewBox="0 0 24 24"><circle cx="12" cy="12" r="10"/></svg>www.larkspurrow.com</li>
      </ul>
    </div>
    <svg class="divider-wedge" viewBox="0 0 50 446" preserveAspectRatio="none" aria-hidden="true">
      <rect x="0" y="0" width="50" height="446" fill="#ffffff"/>
      <polygon points="10,0 12,0 38,446 14,446" fill="var(--wedge-blue)"/>
    </svg>
    <div class="wordmark">Larkspurrow<br>Interiors</div>
  </section>
</body>
</html>
```